"Harbor Constructors" is a residential building company and needs a new business card design and may re

We would like a redesign based on the existing logo, and would like to see a new font as well. We are bespoke home builders who build sustainable energy efficient homes.

Industry/Entity Type

Construction

Contact Information for Business Card

Business card size 40mm x 90mm

Colors

Designer to choose colors to be used in the design.

```html
<!DOCTYPE html>
<html lang="en">
<head>
<meta charset="utf-8">
<title>Harbor Constructors – Business Card</title>
<link rel="stylesheet" href="https://fonts.googleapis.com/css2?family=Open+Sans:wght@400;600;700&display=swap">
<style>
  :root {
    --backdrop: #3a332f;
    --card: #161616;
    --card-edge: #222222;
    --lime: #b5d334;
    --white: #f4f4f4;
    --muted: #8d8d8d;
    --divider: #5a5a5a;
  }
  * { box-sizing: border-box; margin: 0; padding: 0; }
  html, body {
    width: 1200px; height: 864px; overflow: hidden;
    background: var(--backdrop);
    font-family: "Open Sans", sans-serif;
  }
  .canvas { position: relative; width: 1200px; height: 864px; }

  .card {
    position: absolute;
    width: 540px; height: 240px;
    background: var(--card);
    border: 1px solid var(--card-edge);
    box-shadow: 0 18px 40px rgba(0,0,0,.45);
  }

  /* Front */
  .card-front { left: 50px; top: 140px; }
  .front-brand {
    position: absolute; left: 70px; top: 70px;
    display: flex; align-items: center; gap: 18px;
  }
  .brand-square { width: 34px; height: 34px; background: var(--muted); }
  .brand-name {
    font-size: 34px; font-weight: 600; color: var(--muted);
    letter-spacing: .5px; line-height: 1;
  }
  .front-web {
    position: absolute; left: 70px; top: 168px;
    font-size: 13px; letter-spacing: 2.4px; color: var(--muted);
  }

  /* Back */
  .card-back { left: 610px; top: 400px; }
  .back-brand {
    position: absolute; left: 28px; top: 0; height: 100%; width: 210px;
    display: flex; align-items: center; gap: 12px;
  }
  .back-brand .brand-square { width: 26px; height: 26px; background: var(--lime); flex: none; }
  .back-brand .brand-name { font-size: 21px; color: var(--white); font-weight: 700; line-height: 1.15; }
  .divider {
    position: absolute; left: 250px; top: 22px; bottom: 22px;
    width: 1px; background: linear-gradient(to bottom, transparent, var(--divider) 20%, var(--divider) 80%, transparent);
  }
  .details {
    position: absolute; left: 268px; top: 30px;
    color: var(--white); font-size: 12.5px; line-height: 17px;
  }
  .person-name { color: var(--lime); font-weight: 700; font-size: 14px; text-transform: uppercase; margin-bottom: 3px; }
  .company { font-weight: 700; }
  .contact-row { display: flex; align-items: center; gap: 7px; }
  .contact-row svg { width: 11px; height: 11px; flex: none; }
</style>
</head>
<body>
<main class="canvas">
  <section class="card card-front" aria-label="Card front">
    <div class="front-brand">
      <span class="brand-square"></span>
      <span class="brand-name">Harbor Constructors</span>
    </div>
    <p class="front-web">www.harborconstructors.com.au</p>
  </section>

  <section class="card card-back" aria-label="Card back">
    <div class="back-brand">
      <span class="brand-square"></span>
      <span class="brand-name">Harbor Constructors</span>
    </div>
    <div class="divider"></div>
    <div class="details">
      <p class="person-name">Daniel Marlowe</p>
      <p class="company">Harbor Constructors Pty Ltd</p>
      <p>PO Box 2187 Eastgate</p>
      <p>LPO Riverton WA 6148</p>
      <p>Registration 48391</p>
      <p>ABN: 42 305 718 664</p>
      <p class="contact-row">
        <svg viewBox="0 0 12 12" aria-hidden="true"><rect x="3" y="0.5" width="6" height="11" rx="1" fill="none" stroke="#b5d334" stroke-width="1.4"/><rect x="5" y="9" width="2" height="1.2" fill="#b5d334"/></svg>
        0491 570 156
      </p>
      <p class="contact-row">
        <svg viewBox="0 0 12 12" aria-hidden="true"><rect x="0.5" y="2.5" width="11" height="7.5" fill="#b5d334"/><path d="M0.5 2.5 L6 7 L11.5 2.5" fill="none" stroke="#161616" stroke-width="1"/></svg>
        daniel@harborconstructors.com.au
      </p>
      <p class="contact-row">
        <svg viewBox="0 0 12 12" aria-hidden="true"><circle cx="6" cy="6" r="5.5" fill="#b5d334"/><path d="M1 6 H11 M6 0.5 C3 3.5 3 8.5 6 11.5 M6 0.5 C9 3.5 9 8.5 6 11.5" fill="none" stroke="#161616" stroke-width=".9"/></svg>
        www.harborconstructors.com.au
      </p>
    </div>
  </section>
</main>
</body>
</html>
```